KdK Marine Flyer Design Project

Hi we are a marine company based in Dubai. Im looking for a flyer which represents differant aspcts of of service lines... Tobel-Wane Boats, Marine Parts, Sailing Clothes, New&Used boats.

All can be found on our Website .. www.kdkmarine.example .. its basically taking our website info onto a flyer.

```html
<!DOCTYPE html>
<html lang="en">
<head>
<meta charset="utf-8">
<title>KdK Marine — Flyer</title>
<link rel="stylesheet" href="https://fonts.googleapis.com/css2?family=Arimo:wght@400;700&family=Oswald:wght@400;500&display=swap">
<style>
  :root {
    --rust: #c2502c;
    --rust-dark: #9e3a1f;
    --pill-red: #cf3a1a;
    --ocean: #2b8aa8;
    --ocean-deep: #1d6a88;
    --cream: #f6d9a6;
    --gold: #f0b860;
    --email-orange: #f7a23a;
    --white: #ffffff;
  }
  * { margin: 0; padding: 0; box-sizing: border-box; }
  html, body { width: 928px; height: 1200px; overflow: hidden; background: var(--white); }
  .flyer {
    position: relative;
    width: 928px;
    height: 1200px;
    overflow: hidden;
    font-family: "Arimo", Arial, sans-serif;
    color: var(--white);
  }
  .backdrop { position: absolute; inset: 0; }

  .brand {
    position: absolute;
    left: 283px;
    top: 24px;
    font-family: "Oswald", sans-serif;
    font-weight: 500;
    font-size: 62px;
    letter-spacing: 6px;
    text-transform: uppercase;
    color: var(--white);
    line-height: 1;
  }
  .brand-rule {
    position: absolute;
    left: 508px;
    top: 128px;
    width: 290px;
    height: 4px;
    background: linear-gradient(90deg, var(--email-orange), var(--white));
  }
  .contact {
    position: absolute;
    left: 510px;
    top: 142px;
    font-family: "Oswald", sans-serif;
    font-weight: 400;
    font-size: 20px;
    line-height: 32px;
  }
  .contact .label { color: var(--white); text-transform: uppercase; }
  .contact .value { color: var(--email-orange); }
  .contact .tel { padding-left: 14px; }
  .contact .tel .label { color: var(--email-orange); text-transform: none; }
  .contact .tel .value { color: var(--cream); }

  .service-lines {
    position: absolute;
    left: 40px;
    top: 150px;
    width: 430px;
    list-style: none;
    font-family: "Oswald", sans-serif;
    font-weight: 400;
    font-size: 21px;
    line-height: 30px;
    color: var(--cream);
    text-transform: uppercase;
    letter-spacing: 0.5px;
  }
  .service-lines li::before {
    content: "";
    display: inline-block;
    width: 8px;
    height: 8px;
    margin: 0 10px 3px 0;
    background: var(--email-orange);
    border-radius: 50%;
  }

  .category { position: absolute; }
  .category h2 {
    display: inline-block;
    background: var(--pill-red);
    color: var(--white);
    font-family: "Arimo", sans-serif;
    font-weight: 400;
    font-size: 19px;
    line-height: 22px;
    padding: 0 12px 0 8px;
    border-radius: 0 11px 11px 0;
    text-transform: uppercase;
  }
  .category ul { list-style: none; }
  .category li {
    font-size: 19px;
    line-height: 21px;
    letter-spacing: -0.2px;
  }
  .exterior  { left: 39px;  top: 386px; }
  .engine    { left: 283px; top: 326px; }
  .interior  { left: 480px; top: 313px; }
  .utilities { left: 670px; top: 307px; }
  .deck      { left: 670px; top: 458px; }

  .web-pill {
    position: absolute;
    left: 558px;
    top: 1112px;
    width: 390px;
    height: 88px;
    background: var(--pill-red);
    border-radius: 44px 0 0 44px;
    display: flex;
    align-items: center;
    padding-left: 24px;
    font-family: "Oswald", sans-serif;
    font-weight: 400;
    font-size: 34px;
    color: var(--white);
    white-space: nowrap;
  }
</style>
</head>
<body>
<main class="flyer">
  <svg class="backdrop" width="928" height="1200" viewBox="0 0 928 1200">
    <defs>
      <linearGradient id="rustFade" x1="0" y1="0" x2="0" y2="1">
        <stop offset="0" stop-color="#cc5a32"/>
        <stop offset="1" stop-color="#a9401f"/>
      </linearGradient>
      <linearGradient id="oceanFade" x1="0" y1="0" x2="0" y2="1">
        <stop offset="0" stop-color="#2f94b3"/>
        <stop offset="1" stop-color="#1f6f8e"/>
      </linearGradient>
      <linearGradient id="swoosh" x1="0" y1="0" x2="1" y2="0">
        <stop offset="0" stop-color="#f3c27a"/>
        <stop offset="1" stop-color="#fbe6c2"/>
      </linearGradient>
      <linearGradient id="leather" x1="0" y1="0" x2="1" y2="1">
        <stop offset="0" stop-color="#b97a48"/>
        <stop offset="0.5" stop-color="#8c5230"/>
        <stop offset="1" stop-color="#4a2a18"/>
      </linearGradient>
    </defs>
    <rect class="band-top" x="0" y="0" width="928" height="460" fill="url(#rustFade)"/>
    <path class="band-ocean" d="M0,390 C300,330 620,280 928,262 L928,660 C620,690 300,760 0,835 Z" fill="url(#oceanFade)"/>
    <path class="band-swoosh" d="M0,375 C300,315 620,262 928,244 L928,266 C620,285 300,340 0,405 Z" fill="url(#swoosh)"/>
    <path class="band-divider" d="M0,836 C300,762 620,692 928,660" fill="none" stroke="#fdf3e6" stroke-width="16"/>
    <path class="photo-cockpit" role="img" aria-label="Photo of a Tobel-Wane sport boat cockpit with tan leather seats, dashboard gauges and steering wheel"
          d="M0,848 C300,774 620,704 928,672 L928,1200 L0,1200 Z" fill="url(#leather)"/>
  </svg>

  <div class="brand">KdK Marine</div>
  <div class="brand-rule"></div>

  <div class="contact">
    <div><span class="label">Email us now at:</span> <span class="value">info@kdkmarine.example</span></div>
    <div class="tel"><span class="label">Tel:</span> <span class="value">+971500000000</span></div>
  </div>

  <ul class="service-lines">
    <li>Tobel-Wane Boats</li>
    <li>Marine Parts</li>
    <li>Sailing Clothes</li>
    <li>New &amp; Used Boats</li>
  </ul>

  <section class="category exterior">
    <h2>Exterior</h2>
    <ul>
      <li>Exterior lighting</li><li>Underwater lighting</li><li>Searchlights</li><li>Horns &amp; hailers</li>
      <li>Wiper systems</li><li>Navigation lighting</li><li>Hardware</li><li>Chairs</li>
      <li>Adhesives/deck caulks</li><li>Antenna's</li><li>Electrical systems</li><li>Floor protection</li>
      <li>Varnishes/teak oils</li>
    </ul>
  </section>

  <section class="category engine">
    <h2>Engine room</h2>
    <ul>
      <li>Exhaust systems</li><li>Filters</li><li>Batteries</li><li>Battery chargers</li><li>Pumps</li>
      <li>Hoses</li><li>Blowers</li><li>Strainers/fittings</li><li>Bearings</li><li>Engine control</li>
      <li>Steering systems</li><li>Floor protection</li><li>Generators</li>
    </ul>
  </section>

  <section class="category interior">
    <h2>Interior</h2>
    <ul>
      <li>Interior lighting</li><li>Helmsman chairs</li><li>Electrical systems</li><li>Windows</li>
      <li>Toilets</li><li>Adhesives</li><li>Hardware</li><li>Steering wheels</li><li>Floor protection</li>
    </ul>
  </section>

  <section class="category utilities">
    <h2>Utilities</h2>
    <ul>
      <li>Airconditioning</li><li>Power management</li><li>Toilet systems</li><li>Water treatment</li>
    </ul>
  </section>

  <section class="category deck">
    <h2>Deck systems</h2>
    <ul>
      <li>Windlasses &amp; winches</li><li>Cranes &amp; Davits</li><li>Passerelles &amp; transom lifts</li><li>Anchors &amp; chain</li>
    </ul>
  </section>

  <div class="web-pill">www.kdkmarine.example</div>
</main>
</body>
</html>
```